New business card design to go with our new logo

just want an eye-catching business card to go with our new logo. We are open to double sided or single sided. Just want it to have the following info on it. Whatever layout you think looks best.

First and Last Name
Title
Phone 801-555-0187
Address 312 W. Larkmoor Avenue Orem UT 84057
Email thecrew@meadowstailandkennel.example

Industry/Entity Type

Business

```html
<!DOCTYPE html>
<html lang="en">
<head>
<meta charset="utf-8">
<title>Meadows Tail &amp; Kennel — Business Card</title>
<link rel="stylesheet" href="https://fonts.googleapis.com/css2?family=Arimo:wght@400;700&display=swap">
<style>
  :root {
    --sky: #2fa5dc;
    --tangerine: #f68b4c;
    --paper: #ffffff;
    --backdrop: #e7e5e2;
    --ink-white: #ffffff;
  }
  * { box-sizing: border-box; margin: 0; padding: 0; }
  html, body {
    width: 1200px;
    height: 902px;
    overflow: hidden;
    background: var(--backdrop);
    font-family: "Arimo", Arial, sans-serif;
  }
  .card {
    position: absolute;
    left: 80px;
    top: 155px;
    width: 1040px;
    height: 592px;
    background: var(--paper);
    box-shadow: 0 6px 24px rgba(0,0,0,0.12);
  }
  .brand {
    position: absolute;
    left: 0;
    right: 0;
    top: 150px;
    display: flex;
    align-items: center;
    justify-content: center;
    gap: 18px;
  }
  .brand-dot {
    width: 56px;
    height: 56px;
    border-radius: 50%;
    background: var(--sky);
    flex: none;
  }
  .brand-name {
    color: var(--tangerine);
    font-weight: 700;
    font-size: 44px;
    letter-spacing: 0.5px;
  }
  .name-band {
    position: absolute;
    left: 0;
    top: 346px;
    width: 100%;
    height: 58px;
    display: flex;
  }
  .name-band .person {
    width: 520px;
    background: var(--sky);
    color: var(--ink-white);
    font-weight: 700;
    font-size: 30px;
    text-align: right;
    padding-right: 33px;
    line-height: 58px;
  }
  .name-band .role {
    flex: 1;
    margin-left: 2px;
    background: var(--tangerine);
    color: var(--ink-white);
    font-size: 24px;
    padding-left: 37px;
    line-height: 58px;
  }
  .contact {
    position: absolute;
    left: 56px;
    top: 474px;
    color: var(--sky);
    font-size: 24px;
  }
  .contact li {
    list-style: none;
    display: flex;
    align-items: center;
    gap: 10px;
    height: 36px;
  }
  .contact svg { width: 32px; height: 32px; flex: none; }
  .address {
    position: absolute;
    left: 676px;
    top: 476px;
    color: var(--sky);
    font-size: 24px;
    line-height: 33px;
    font-style: normal;
  }
</style>
</head>
<body>
  <section class="card">
    <div class="brand">
      <span class="brand-dot"></span>
      <span class="brand-name">Meadows Tail &amp; Kennel</span>
    </div>

    <div class="name-band">
      <div class="person">JORDAN HALE</div>
      <div class="role">Founder</div>
    </div>

    <ul class="contact">
      <li>
        <svg viewBox="0 0 32 32" aria-hidden="true">
          <circle cx="16" cy="16" r="14" fill="none" stroke="var(--tangerine)" stroke-width="2"/>
          <path d="M9 13c0-2 3-3 7-3s7 1 7 3v1h-3v-1.5c-1-.5-2.5-.7-4-.7s-3 .2-4 .7V14H9z" fill="var(--tangerine)"/>
          <rect x="10" y="15" width="12" height="7" rx="1.5" fill="var(--tangerine)"/>
          <circle cx="16" cy="18.5" r="1.8" fill="#fff"/>
        </svg>
        <span>801-555-0187</span>
      </li>
      <li>
        <svg viewBox="0 0 32 32" aria-hidden="true">
          <circle cx="16" cy="16" r="14" fill="none" stroke="var(--tangerine)" stroke-width="2"/>
          <rect x="9" y="11" width="14" height="10" rx="1" fill="var(--tangerine)"/>
          <path d="M9.5 11.5 16 17l6.5-5.5" fill="none" stroke="#fff" stroke-width="1.4"/>
        </svg>
        <span>thecrew@meadowstailandkennel.example</span>
      </li>
    </ul>

    <address class="address">
      312 W. Larkmoor Avenue<br>
      Orem UT 84057
    </address>
  </section>
</body>
</html>
```